Business Card for a Life Coaching Company

BRAVOPEAK is a Life Coaching company that was initiated to support people who want to transform thier life or ana aspect of it.
our slogan is : "Dream. Believe. Succeed"
our logo is uploaded.
The name of the company implies that leadership, strength and wisdom required to change your life.
We want an attractive business card that would give an impression of reliability, support and change. so we really want it unique. Here are some examples of unique cards:

http://www.cardcraftvault.example/2009/05/100-really-creative-business-cards/

BravoPeak is a life coaching organization focusing on individual transformation through the application of relevant and timeless principles of success.  BravoPeak believes that real, sustainable life transformations are brought about by tuning into the timeless wisdom we each carry in our hearts while boldy acting in the direction of our dreams.

Contacts on the card:
Address: 7 Tarek Nour El Dine Heliopolis Cairo Egypt
Tel: +202 24 71 38 52
Fax: +202 24 71 38 17
Mobile: +2 012 684 2097 (Dalia Soliman)
+2 0199915815 (Tariq Bhatti)

By the way, our temporary website is http://www.bravopeak.example

We have attached an .eps file with various configurations of our logo.

```html
<!DOCTYPE html>
<html lang="en">
<head>
<meta charset="utf-8">
<title>BravoPeak Business Card</title>
<link rel="stylesheet" href="https://fonts.googleapis.com/css2?family=Cinzel:wght@400&family=Tenor+Sans&display=swap">
<style>
  :root {
    --paper: #ffffff;
    --frame: #b9b9b9;
    --orange: #e05a24;
    --sun-core: #f7b21a;
    --sun-mid: #ee8a1c;
    --slate: #8e9092;
    --slate-light: #a3a3a3;
    --ink-light: #ffffff;
  }
  * { margin: 0; padding: 0; box-sizing: border-box; }
  html, body {
    width: 1200px;
    height: 695px;
    overflow: hidden;
    background: var(--paper);
  }
  .card {
    position: relative;
    width: 1200px;
    height: 695px;
    background: var(--paper);
    border: 2px solid var(--frame);
  }
  .panel-warm {
    position: absolute;
    left: 32px; top: 30px;
    width: 455px; height: 632px;
    background: var(--orange);
    overflow: hidden;
  }
  .sunburst {
    position: absolute;
    left: 205px; top: 40px;
    width: 500px; height: 500px;
    border-radius: 50%;
    background: radial-gradient(circle at center,
      var(--sun-core) 0%,
      var(--sun-mid) 30%,
      rgba(224, 90, 36, 0) 70%);
  }
  .panel-slate {
    position: absolute;
    left: 491px; top: 30px;
    width: 677px; height: 632px;
    background: linear-gradient(to right, var(--slate), var(--slate-light));
  }
  .slogan-band-left {
    position: absolute;
    left: 32px; top: 482px;
    width: 455px; height: 57px;
    background: var(--slate);
  }
  .slogan-band-right {
    position: absolute;
    left: 491px; top: 482px;
    width: 677px; height: 57px;
    background: var(--orange);
  }
  .brand-name {
    position: absolute;
    left: 512px; top: 208px;
    font-family: "Cinzel", serif;
    font-weight: 400;
    font-size: 150px;
    line-height: 116px;
    color: var(--ink-light);
    letter-spacing: -2px;
  }
  .brand-name span { display: block; }
  .slogan {
    position: absolute;
    top: 482px;
    height: 57px;
    line-height: 57px;
    font-family: "Tenor Sans", sans-serif;
    font-size: 29px;
    color: var(--ink-light);
    white-space: pre;
  }
  .slogan-dream { right: calc(1200px - 467px); }
  .slogan-divider {
    position: absolute;
    left: 492px; top: 496px;
    width: 3px; height: 28px;
    background: var(--orange);
  }
  .slogan-rest { left: 537px; }
</style>
</head>
<body>
  <div class="card">
    <div class="panel-warm">
      <div class="sunburst" role="img" aria-label="Warm sunburst glow where the brand symbol sits"></div>
    </div>
    <div class="panel-slate"></div>

    <div class="brand-name">
      <span>BRAVO</span>
      <span>PEAK</span>
    </div>

    <div class="slogan-band-left"></div>
    <div class="slogan-band-right"></div>
    <div class="slogan slogan-dream">"Dream</div>
    <div class="slogan-divider"></div>
    <div class="slogan slogan-rest">Believe  |   Succeed"</div>
  </div>
</body>
</html>
```